New Service Brochure for The Brackenford Spa

Hi All! We are looking for a new brochure design- tri-fold, double sided, and full color. We are a certified Tovrel Spa for men and women in the heart of the Catskill Mountains of upstate New York. Our clients would describe us as laid back luxury with no pretensions and a home away from home vibe. Our font is Avalon. Key colors are black, white and gold. Looking for an inviting, clean, and modern/minimalist spread with a touch of elegance. No orchid imagery, please. I would like our "Tovrel Spa" logo on cover, too please. Front cover image with with logo and "Tovrel Spa" Sticker . Bottom of back with contact info. We would prefer massages go on left inside page, facials in middle and right inside, nails on back left, but we are open to new or different layout proposals. Thank you!

Target Market(s)

Men & Women.

Industry/Entity Type

Health And Wellness

Font styles to use
Other font styles liked:
• Avalon is our signature font

Requirements
Must have
• Easy on the eyes.
Nice to have
• Negative space.
Should not have
• No orchids. Busy lines and wild colors.

```html
<!DOCTYPE html>
<html lang="en">
<head>
<meta charset="utf-8">
<title>The Brackenford Spa – Service Brochure</title>
<link href="https://fonts.googleapis.com/css2?family=Questrial&family=Didact+Gothic&display=swap" rel="stylesheet">
<style>
:root{
  --gold:#c9a227;
  --gold-dark:#a8841a;
  --ink:#2a2a2a;
  --muted:#6b6b6b;
  --panel:#f2f2f2;
  --panel-shade:#e4e4e4;
  --paper:#ffffff;
  --stage:#d9d6d1;
  --badge:#5f9a3a;
}
*{margin:0;padding:0;box-sizing:border-box}
html,body{width:1200px;height:1200px;overflow:hidden}
body{background:var(--stage);font-family:"Didact Gothic",sans-serif;color:var(--ink);position:relative}
.spread{position:absolute;left:30px;width:1140px;height:560px;background:var(--panel);box-shadow:0 6px 18px rgba(0,0,0,.18);overflow:hidden}
.spread--outside{top:25px}
.spread--inside{top:615px}
.panel{position:absolute;top:0;width:380px;height:560px}
.panel--1{left:0;background:linear-gradient(90deg,var(--paper),var(--panel))}
.panel--2{left:380px;background:linear-gradient(90deg,var(--panel-shade),var(--panel) 30%,var(--paper))}
.panel--3{left:760px;background:linear-gradient(90deg,var(--panel-shade),var(--paper) 35%)}
.inside-bg .panel--1{background:linear-gradient(90deg,var(--paper),var(--panel))}
.inside-bg .panel--2{background:var(--panel-shade)}
.inside-bg .panel--3{background:linear-gradient(90deg,var(--panel),var(--paper))}
.layer{position:absolute;left:0;top:0}
.section-title{font-family:"Questrial",sans-serif;color:var(--gold);font-size:13px;letter-spacing:.5px;text-transform:uppercase}
.menu{position:absolute}
.item{margin-top:12px}
.item__head{display:flex;justify-content:space-between;align-items:flex-start;gap:8px}
.item__name{font-family:"Questrial",sans-serif;font-size:10px;text-transform:uppercase;color:var(--ink);letter-spacing:.3px;line-height:1.25}
.item__price{font-family:"Questrial",sans-serif;font-size:12px;color:var(--gold);white-space:nowrap}
.item__desc{font-size:7px;line-height:1.4;color:var(--muted);margin-top:3px}
.item__time{color:var(--gold)}
.menu--icons .item__name{padding-left:16px;position:relative}
.menu--icons .item__name::before{content:"";position:absolute;left:0;top:0;width:10px;height:10px;border-radius:50%;border:2px solid var(--gold);background:var(--paper)}
.intro{font-size:7px;line-height:1.4;color:var(--muted);margin-top:3px}
.brand{font-family:"Questrial",sans-serif;color:var(--ink);text-transform:uppercase;letter-spacing:1.5px}
.cover__brand{position:absolute;top:28px;left:0;width:380px;text-align:center;font-size:15px}
.cover__headline{position:absolute;top:66px;left:0;width:380px;text-align:center;font-family:"Questrial",sans-serif;font-size:17px;line-height:1.3;color:var(--ink);text-transform:uppercase}
.cover__headline em{font-style:normal;color:var(--gold)}
.cover__badge{position:absolute;left:152px;top:368px;width:66px;height:66px;border-radius:50%;background:var(--badge);border:4px solid var(--paper);box-shadow:0 0 0 1px var(--panel-shade)}
.cover__text{position:absolute;top:450px;left:30px;width:320px;text-align:center;font-size:7.5px;line-height:1.45;color:var(--muted)}
.pill{position:absolute;top:492px;left:50%;transform:translateX(-50%);background:var(--gold);color:var(--paper);font-size:8px;letter-spacing:1px;padding:4px 30px;border-radius:10px;white-space:nowrap}
.contact__brand{position:absolute;top:130px;left:0;width:380px;text-align:center;font-size:28px;line-height:1.1}
.contact__tagline{position:absolute;top:200px;left:0;width:380px;text-align:center;font-size:8px;color:var(--muted)}
.contact__call{position:absolute;left:30px;top:382px;font-family:"Questrial",sans-serif;color:var(--gold);font-size:22px;text-transform:uppercase}
.contact__phone{position:absolute;left:30px;top:410px;font-family:"Questrial",sans-serif;color:var(--ink);font-size:25px;font-weight:bold}
.contact__list{position:absolute;left:30px;top:452px;list-style:none;font-size:7px;line-height:1.35;color:var(--muted)}
.contact__list li{display:flex;gap:6px;align-items:flex-start;margin-bottom:4px}
.contact__list svg{flex:none;margin-top:1px}
</style>
</head>
<body>

<!-- Outside of the brochure -->
<section class="spread spread--outside">
  <div class="panel panel--1">
    <div class="menu" style="left:26px;top:24px;width:328px">
      <h2 class="section-title">Hands &amp; Feet</h2>
      <p class="intro">Settle into a pedicure throne in our nail lounge. Our scrubs and masques are made in house with fresh organic ingredients, and every nail service includes polish of choice.</p>

      <div class="item">
        <div class="item__head"><span class="item__name">Organic Eight<br>Greens Manicure</span><span class="item__price">$65</span></div>
        <p class="item__desc">Hydrate and soothe tired, overworked hands with a cleansing blend of eight greens, a fortifying soak and a gentle detox hand treatment. <span class="item__time">55 minutes.</span></p>
      </div>
      <div class="item">
        <div class="item__head"><span class="item__name">Brackenford Spa Pedicure</span><span class="item__price">$75</span></div>
        <p class="item__desc">Our classic pedicure with a soothing anti-inflammatory mud mask, a revitalizing foot and calf massage and your choice of polish. <span class="item__time">55 minutes.</span></p>
      </div>
      <div class="item">
        <div class="item__head"><span class="item__name">Hot Stone Manicure</span><span class="item__price">$65</span></div>
        <p class="item__desc">Dissolve tension and stress with warm stones and a long arm massage. Hands are left soft and smooth with our signature balm. <span class="item__time">55 minutes.</span></p>
      </div>
      <div class="item">
        <div class="item__head"><span class="item__name">Mother of<br>Dragonfruit Pedicure</span><span class="item__price">$85</span></div>
        <p class="item__desc">Banish calluses and reward tired feet. A fruit enzyme soak, gentle exfoliation, polished toes and a warm stone foot and leg massage. <span class="item__time">55 minutes.</span></p>
      </div>
      <div class="item">
        <div class="item__head"><span class="item__name">Reverse the Hands of<br>Time Manicure</span><span class="item__price">$85</span></div>
        <p class="item__desc">Smoothing sugar scrub, brightening masque and a rich tightening hand cream. <span class="item__time">55 minutes.</span></p>
      </div>
      <div class="item">
        <div class="item__head"><span class="item__name">Grapefruit and<br>Pine Pedicure</span><span class="item__price">$85</span></div>
        <p class="item__desc">Meet spring in a pine forest with refreshing, comforting and grounding scents. A perfect pick-me-up for any season with soak, scrub, cuticle and nail care. <span class="item__time">30 minutes.</span></p>
      </div>
    </div>
  </div>

  <div class="panel panel--2"></div>
  <div class="panel panel--3"></div>

  <svg class="layer" style="left:380px" width="760" height="560" viewBox="0 0 760 560" role="img" aria-label="Photograph of a woman receiving a relaxing facial massage">
    <defs>
      <linearGradient id="facial-photo" x1="0" y1="0" x2="1" y2="1">
        <stop offset="0" stop-color="#e9e3de"/>
        <stop offset=".5" stop-color="#d8c2b2"/>
        <stop offset="1" stop-color="#c9c3bf"/>
      </linearGradient>
    </defs>
    <path d="M190,298 C340,280 470,135 760,120 L760,402 C600,425 470,345 300,312 Z" fill="url(#facial-photo)"/>
  </svg>
  <svg class="layer" style="left:380px" width="760" height="560" viewBox="0 0 760 560" aria-hidden="true">
    <path d="M0,300 C230,292 430,128 760,112" fill="none" stroke="var(--gold)" stroke-width="14"/>
    <path d="M190,302 C380,320 520,420 760,398" fill="none" stroke="var(--gold)" stroke-width="12"/>
  </svg>

  <div class="panel" style="left:380px;background:none">
    <div class="brand contact__brand">The<br>Brackenford Spa</div>
    <p class="contact__tagline">a boutique spa for Men &amp; Women</p>
    <svg class="layer" style="left:30px;top:300px" width="80" height="60" role="img" aria-label="Small snail illustration">
      <ellipse cx="40" cy="34" rx="34" ry="22" fill="#e2dcd3"/>
    </svg>
    <p class="contact__call">Call us now</p>
    <p class="contact__phone">(518) 555-0142</p>
    <ul class="contact__list">
      <li><svg width="8" height="8" viewBox="0 0 10 10"><circle cx="5" cy="5" r="5" fill="var(--gold)"/><circle cx="5" cy="4" r="1.6" fill="#fff"/></svg><span>42 Alder Ridge Road<br>Brackenford, NY 12400<br>Just off Main Street</span></li>
      <li><svg width="8" height="8" viewBox="0 0 10 10"><circle cx="5" cy="5" r="5" fill="var(--gold)"/><rect x="2.5" y="3.3" width="5" height="3.4" fill="#fff"/></svg><span>info@brackenfordspa.com</span></li>
      <li><svg width="8" height="8" viewBox="0 0 10 10"><circle cx="5" cy="5" r="5" fill="var(--gold)"/><circle cx="5" cy="5" r="2.4" fill="none" stroke="#fff"/></svg><span>www.brackenfordspa.com</span></li>
    </ul>
  </div>

  <div class="panel" style="left:760px;background:none">
    <div class="brand cover__brand">The Brackenford Spa</div>
    <h1 class="cover__headline">Escape the <em>Congestion</em><br>of <em>Everyday</em> Life</h1>
    <div class="cover__badge" role="img" aria-label="Certification badge"></div>
    <p class="cover__text">Located in the heart of the Catskill Mountains, our down-to-earth staff, laid back atmosphere and extraordinary services leave no room for pretenses.</p>
    <span class="pill">www.brackenfordspa.com</span>
  </div>
</section>

<!-- Inside of the brochure -->
<section class="spread spread--inside inside-bg">
  <div class="panel panel--1"></div>
  <div class="panel panel--2"></div>
  <div class="panel panel--3"></div>

  <svg class="layer" width="1140" height="560" viewBox="0 0 1140 560" role="img" aria-label="Photographs of a woman resting on a massage table and a man receiving a back massage">
    <defs>
      <linearGradient id="massage-photo" x1="0" y1="0" x2="1" y2="0">
        <stop offset="0" stop-color="#e8e2da"/>
        <stop offset=".35" stop-color="#d6bfa9"/>
        <stop offset=".7" stop-color="#c9a88e"/>
        <stop offset="1" stop-color="#e6ded6"/>
      </linearGradient>
    </defs>
    <path d="M0,0 H1140 V225 C1010,240 900,205 720,160 C580,128 420,128 0,128 Z" fill="url(#massage-photo)"/>
  </svg>
  <svg class="layer" width="1140" height="560" viewBox="0 0 1140 560" aria-hidden="true">
    <path d="M0,18 C150,5 300,8 420,30" fill="none" stroke="var(--gold)" stroke-width="10"/>
    <path d="M0,134 C420,134 580,134 720,166 C900,210 1010,246 1140,230" fill="none" stroke="var(--gold)" stroke-width="10"/>
    <path d="M0,142 C420,142 580,142 720,174 C900,218 1010,254 1140,238" fill="none" stroke="var(--ink)" stroke-width="2"/>
  </svg>

  <div class="menu menu--icons" style="left:24px;top:156px;width:330px">
    <h2 class="section-title">Massage</h2>
    <div class="item">
      <div class="item__head"><span class="item__name">Tension Tamer</span><span class="item__price">$125/$195</span></div>
      <p class="item__desc">Head, neck and shoulders. Deep tissue with hot towels, muscle soothing oils and cupping. <span class="item__time">55 or 90 minutes.</span></p>
    </div>
    <div class="item">
      <div class="item__head"><span class="item__name">Prenatal</span><span class="item__price">$135/$175</span></div>
      <p class="item__desc">Ultimate treat for mothers-to-be. Soothes aches and pains during pregnancy. Mother must be out of first trimester. <span class="item__time">55 minutes.</span></p>
    </div>
    <div class="item">
      <div class="item__head"><span class="item__name">Pulsewave Rapid<br>Recovery Massage</span><span class="item__price">$135</span></div>
      <p class="item__desc">Recover faster and feel better while optimizing your massage time with dynamic compression. Mobilizes fluid, speeds recovery and eases aching muscles, with focused neck, shoulder, arm and hand massage. <span class="item__time">55 minutes.</span></p>
    </div>
    <div class="item">
      <div class="item__head"><span class="item__name">Swedish Massage</span><span class="item__price">$105/$160</span></div>
      <p class="item__desc">Relaxing and therapeutic. Eases tension and enhances circulation. Great for a first-time massage or any day off. <span class="item__time">55 or 90 minutes.</span></p>
    </div>
    <div class="item">
      <div class="item__head"><span class="item__name">Recovery</span><span class="item__price">$110/$170</span></div>
      <p class="item__desc">Specific to your athletic needs, whether pro or weekend warrior. Relax, stretch and recover. <span class="item__time">55 or 90 minutes.</span></p>
    </div>
    <div class="item">
      <div class="item__head"><span class="item__name">Deep Tissue</span><span class="item__price">$115/$175</span></div>
      <p class="item__desc">A therapeutic combination of slow and deep pressure that relieves chronic pain, muscle fatigue and limited range of motion. Muscle therapy lotion or creme. <span class="item__time">55 or 90 minutes.</span></p>
    </div>
  </div>

  <div class="menu menu--icons" style="left:404px;top:196px;width:330px">
    <h2 class="section-title">Facials</h2>
    <div class="item">
      <div class="item__head"><span class="item__name">Detox Facial</span><span class="item__price">$135</span></div>
      <p class="item__desc">Organically remove damage, congestion and imperfections. Ideal for blemishes that won't heal, acne and fine lines. Increases oxygen and blood flow to reboot your skin's natural healing abilities. <span class="item__time">55 minutes.</span></p>
    </div>
    <div class="item">
      <div class="item__head"><span class="item__name">B.L.T. Facial</span><span class="item__price">$145</span></div>
      <p class="item__desc">Brighten. Lighten. Tighten. An organic triple peel, also known as our runway peel, because it leaves you glowing and ready for the red carpet immediately. Ideal for treating hyper-pigmentation. <span class="item__time">55 minutes.</span></p>
    </div>
    <div class="item">
      <div class="item__head"><span class="item__name">Double Down Facial</span><span class="item__price">$165</span></div>
      <p class="item__desc">Who says you can't multitask and relax? Detox, tighten and increase circulation with our all-time favorite peel, followed by our top of the line multi-acid peel. Resurface, smooth, brighten and hydrate. Head, neck and arm massage included. <span class="item__time">55 minutes.</span></p>
    </div>
    <div class="item">
      <div class="item__head"><span class="item__name">Organic Masque Montage</span><span class="item__price">$115</span></div>
      <p class="item__desc">Three layers of customized masques created exclusively for your skin type. Includes steam, cleanse, exfoliation, extractions, masques, massage and moisturizer. <span class="item__time">55 minutes.</span></p>
    </div>
  </div>

  <div class="menu menu--icons" style="left:784px;top:262px;width:330px">
    <div class="item">
      <div class="item__head"><span class="item__name">Calm Skin Facial</span><span class="item__price">$125</span></div>
      <p class="item__desc">Rosacea and sensitive skin be damned! This facial was made for you. Combats redness, irritation and dryness. Gentle yet effective for the most sensitive skin types. <span class="item__time">55 minutes.</span></p>
    </div>
    <div class="item">
      <div class="item__head"><span class="item__name">R&amp;R Facial</span><span class="item__price">$255 (REG. $275)</span></div>
      <p class="item__desc">Radiance and Revenge. Let's cut to the chase: our most dynamic results-oriented facial, the ultimate kick start to reversing skin after a long summer of sunshine. Microdermabrasion, double peel and light therapy. <span class="item__time">90 minutes.</span></p>
    </div>
    <div class="item">
      <div class="item__head"><span class="item__name">Mangosteen Facial</span><span class="item__price">$135</span></div>
      <p class="item__desc">Minimize pore size and surface build up with zero downtime. Our organic lactic acid peel leaves skin smooth, calm and glowing. Custom masque included. Ideal for all skin types. <span class="item__time">55 minutes.</span></p>
    </div>
  </div>
</section>

</body>
</html>
```